Create a memorable Stationary for Security Software Company

TelVandrik is the worldwide leader in securing the Internet. Making Internet communications and critical data secure, reliable and available everywhere has been and continues to be our ongoing vision. We are committed to staying focused on real customer needs and to developing new and innovative security solutions that redefine the security landscape.

Industry/Entity Type

Internet

Font styles to use
Serif
Sans Serif
Script

Colors
0792cd
33a6d7
85cae6

```html
<!DOCTYPE html>
<html lang="en">
<head>
<meta charset="utf-8">
<title>TelVandrik Stationery</title>
<link href="https://fonts.googleapis.com/css2?family=Lato:wght@400;700&family=Mrs+Saint+Delafield&display=swap" rel="stylesheet">
<style>
  :root{
    --blue-deep:#0792cd;
    --blue-mid:#33a6d7;
    --blue-light:#85cae6;
    --folder:#4bb6e0;
    --ink:#333a40;
    --ink-soft:#555c63;
    --paper:#ffffff;
    --bg:#e4e8ea;
  }
  html,body{margin:0;padding:0;overflow:hidden;}
  body{width:1200px;height:910px;background:radial-gradient(ellipse at 50% 30%,#eef1f2 0%,var(--bg) 70%);font-family:'Lato',sans-serif;position:relative;}
  .sheet{position:absolute;box-sizing:border-box;}
  .wordmark{display:flex;align-items:center;gap:6px;color:var(--blue-deep);font-family:'Lato',sans-serif;font-weight:700;}
  .wordmark .dot{border-radius:50%;background:var(--blue-deep);flex:none;}

  .card-front{left:189px;top:81px;width:203px;height:107px;border-radius:10px;background:radial-gradient(ellipse at 50% 45%,var(--blue-light) 0%,var(--blue-mid) 45%,var(--blue-deep) 100%);display:flex;align-items:center;justify-content:center;}
  .card-front .wordmark{color:#0a6f9c;font-size:15px;}
  .card-front .wordmark .dot{width:12px;height:12px;background:#0a6f9c;}

  .card-back{left:421px;top:81px;width:203px;height:107px;border-radius:10px;background:var(--paper);padding:13px 14px;}
  .card-back .name{color:var(--blue-deep);font-size:12px;margin:0;}
  .card-back .role{font-size:6px;color:var(--ink-soft);margin:2px 0 0;}
  .card-back .contact{position:absolute;left:14px;bottom:12px;font-size:6.8px;color:var(--ink);line-height:9px;margin:0;list-style:none;padding:0;}
  .label{color:var(--blue-deep);display:inline-block;width:10px;}
  .card-back .wordmark{position:absolute;right:12px;bottom:18px;font-size:9px;gap:4px;}
  .card-back .wordmark .dot{width:7px;height:7px;}

  .letterhead{left:170px;top:243px;width:399px;height:543px;border-radius:8px;background:var(--paper);padding:0 60px 0 43px;}
  .letterhead .wordmark{position:absolute;left:43px;top:62px;font-size:14px;}
  .letterhead .wordmark .dot{width:11px;height:11px;}
  .greeting{position:absolute;left:43px;top:137px;margin:0;font-size:10px;color:var(--ink);}
  .body-copy{position:absolute;left:43px;top:172px;width:296px;margin:0;}
  .body-copy p{font-size:6.7px;line-height:10.8px;color:var(--ink-soft);text-align:justify;margin:0 0 11px;}
  .signoff{position:absolute;left:43px;top:363px;}
  .signoff .name{font-size:10px;color:var(--ink);margin:0;}
  .signoff .role{font-size:6px;color:var(--ink-soft);margin:4px 0 0;}
  .signature{position:absolute;left:36px;top:400px;font-family:'Mrs Saint Delafield',cursive;font-size:30px;color:#333;margin:0;}
  .letter-footer{position:absolute;left:43px;top:501px;font-size:6.4px;color:var(--ink);display:flex;gap:18px;margin:0;padding:0;list-style:none;}
  .letter-footer .label{width:auto;margin-right:5px;}

  .folder{left:631px;top:243px;width:399px;height:543px;}
  .folder svg{position:absolute;left:0;top:0;}
  .folder .wordmark{position:absolute;left:0;right:0;top:215px;justify-content:center;color:#1f8fc4;font-size:22px;gap:8px;}
  .folder .wordmark .dot{width:16px;height:16px;background:#1f8fc4;}
</style>
</head>
<body>
  <section class="sheet card-front" aria-label="Business card front">
    <div class="wordmark"><span class="dot"></span>TelVandrik</div>
  </section>

  <section class="sheet card-back" aria-label="Business card back">
    <p class="name">Mara Lindqvist</p>
    <p class="role">Co-Founder &amp; CEO</p>
    <ul class="contact">
      <li><span class="label">T:</span>(404) 555-0188</li>
      <li><span class="label">M:</span>mara@telvandrik.net</li>
      <li><span class="label">W:</span>telvandrik.net</li>
    </ul>
    <div class="wordmark"><span class="dot"></span>TelVandrik</div>
  </section>

  <section class="sheet letterhead" aria-label="Letterhead">
    <div class="wordmark"><span class="dot"></span>TelVandrik</div>
    <p class="greeting">Dear Mr. Halvorsen,</p>
    <div class="body-copy">
      <p>Lorem ipsum dolor sit amet, consectetur adipiscing elit. Donec orci purus, luctus vitae dignissim eu, iaculis sed purus. Vivamus faucibus, ipsum nec aliquet viverra, leo mauris condimentum ligula, sit amet sagittis enim ligula quis arcu. Nam egestas tortor id nisi porttitor mattis. In tortor ante, ultricies in suscipit a, tempus non massa. Vivamus et auctor mi. Fusce vel massa nulla. Phasellus nec eros mauris, et scelerisque orci. Donec malesuada orci vitae nulla accumsan porta a id massa. Quisque accumsan iaculis magna sit amet fringilla. Maecenas consequat, magna eget tincidunt semper, odio nibh rutrum mi, id feugiat ante nisi eu risus. Vestibulum nunc orci, rhoncus a placerat in, ultricies in mi. Cras mattis varius eros, vel fringilla nisi suscipit eget.</p>
      <p>Quisque scelerisque sagittis nulla at porttitor. Mauris a justo et tellus interdum tristique. Sed id augue vitae urna euismod commodo aliquet a quam. Pellentesque arcu velit, cursus et malesuada ut, consequat et diam. Nullam erat sem, rhoncus id ullamcorper vitae, rhoncus et arcu. In ultricies ultricies nulla, ut rutrum nisi iaculis at. Donec eu magna a metus ornare faucibus. Fusce aliquet faucibus ultricies. Morbi semper, est id tincidunt gravida, sem arcu adipiscing lacus, ac bibendum nulla leo eu purus. Quisque nec diam sed risus consectetur a cumsan quis quis nibh. Vestibulum id purus lorem.</p>
    </div>
    <div class="signoff">
      <p class="name">Mara Lindqvist</p>
      <p class="role">Co-Founder &amp; CEO</p>
    </div>
    <p class="signature">Mara Lindqvist</p>
    <ul class="letter-footer">
      <li><span class="label">T:</span>(404) 555-0188</li>
      <li><span class="label">M:</span>mara@telvandrik.net</li>
      <li><span class="label">W:</span>telvandrik.net</li>
    </ul>
  </section>

  <section class="sheet folder" aria-label="Presentation folder">
    <svg width="399" height="543" viewBox="0 0 399 543">
      <defs>
        <linearGradient id="folderFill" x1="0" y1="0" x2="0" y2="1">
          <stop offset="0" stop-color="#55c0e4"/>
          <stop offset="1" stop-color="#45b1de"/>
        </linearGradient>
      </defs>
      <rect x="0" y="0" width="399" height="543" rx="8" fill="url(#folderFill)"/>
      <path d="M399 118 C380 122 372 130 372 146 L372 246 C372 262 380 270 399 274" fill="none" stroke="#3fa6d3" stroke-width="2"/>
      <path d="M399 118 C380 122 372 130 372 146 L372 246 C372 262 380 270 399 274 Z" fill="#47afda"/>
    </svg>
    <div class="wordmark"><span class="dot"></span>TelVandrik</div>
  </section>
</body>
</html>
```